Business Card Design - Kestrel Tidewave

We (Kestrel Tidewave) need a business card design for our boutique mobile marketing agency based in Sydney, Australia.
We work with brands and advertisers to deliver and implement end to end mobile (smartphone and tablet) marketing solutions.

We already have a logo and website design, these files will be provided. Our colours centre around a blue/orange mix (the logo containing the orange (colour code: RGB 255,165,0).

Our name and logo communicate strength and confidence. We see ourselves as being trustworthy advisors who are also fun and passionate.

Target Market(s)

Senior Marketing Managers

Industry/Entity Type

Marketing

Requirements
Must have
• Employee Name: Tobin Ashgrove
Mobile Number: 0400 555 182
Email Address xxxx@kestreltidewave.example
Website: www.kestreltidewave.example
Twitter ID: KestrelTidewave

```html
<!DOCTYPE html>
<html lang="en">
<head>
<meta charset="utf-8">
<title>Kestrel Tidewave – Business Card</title>
<link rel="stylesheet" href="https://fonts.googleapis.com/css2?family=Open+Sans:wght@400;600;700&display=swap">
<style>
  :root {
    --bg: #000000;
    --orange: #f5893a;
    --ink: #3a3a3a;
    --text: #333333;
    --white: #ffffff;
    --edge: #cfcfcf;
  }
  * { margin: 0; padding: 0; box-sizing: border-box; }
  html, body {
    width: 1200px; height: 960px; overflow: hidden;
    background: var(--bg);
    font-family: "Open Sans", Arial, sans-serif;
  }
  .stage { position: relative; width: 1200px; height: 960px; }
  .card {
    position: absolute; top: 79px;
    width: 363px; height: 652px;
    border-radius: 18px; overflow: hidden;
  }
  .card--front { left: 228px; background: var(--orange); }
  .card--back { left: 634px; background: var(--white); border: 1px solid var(--edge); }

  .wordmark {
    position: absolute; left: 0; right: 0;
    display: flex; align-items: center; justify-content: center; gap: 10px;
    font-weight: 700; color: var(--ink); white-space: nowrap;
  }
  .wordmark__dot { border-radius: 50%; flex: none; }
  .card--front .wordmark { top: 330px; font-size: 30px; }
  .card--front .wordmark__dot { width: 26px; height: 26px; background: var(--white); }
  .card--back .wordmark { top: 280px; font-size: 26px; }
  .card--back .wordmark__dot { width: 22px; height: 22px; background: var(--orange); }

  .contact { position: absolute; left: 17px; top: 412px; right: 8px; }
  .contact__name {
    font-size: 24px; font-weight: 600; color: var(--orange);
    line-height: 1; margin-bottom: 22px;
  }
  .contact__row {
    display: grid; grid-template-columns: 118px 12px 1fr;
    font-size: 14px; color: var(--text); line-height: 1;
    margin-bottom: 19px; white-space: nowrap;
  }
  .web-band {
    position: absolute; left: 0; right: 0; top: 573px; height: 37px;
    background: var(--orange); color: var(--white);
    display: flex; align-items: center; justify-content: center;
    font-size: 16px;
  }
</style>
</head>
<body>
<main class="stage">
  <section class="card card--front" aria-label="Card front">
    <div class="wordmark"><span class="wordmark__dot"></span>Kestrel Tidewave</div>
  </section>

  <section class="card card--back" aria-label="Card back">
    <div class="wordmark"><span class="wordmark__dot"></span>Kestrel Tidewave</div>
    <div class="contact">
      <p class="contact__name">Tobin Ashgrove</p>
      <p class="contact__row"><span>Mobile Number</span><span>:</span><span>0400 555 182</span></p>
      <p class="contact__row"><span>Email Address</span><span>:</span><span>xxxx@kestreltidewave.example</span></p>
      <p class="contact__row"><span>Twitter ID</span><span>:</span><span>KestrelTidewave</span></p>
    </div>
    <div class="web-band">www.kestreltidewave.example</div>
  </section>
</main>
</body>
</html>
```